Brochure 2 fold and Trifold

We need 2 types of brochure (2 fold and Trifold) design for our Brand "VELVET DAWN" Logo (La douceur de Fenor) is in rose gold color
Updates
Target Market(s)
Women ages 17 and up
Industry/Entity Type
Supplement
Font styles to use
Serif
Script
Requirements
Must have
- Rose gold color tone make it look premium, minimalist look

```html
<!DOCTYPE html>
<html lang="en">
<head>
<meta charset="utf-8">
<title>Velvet Dawn Trifold Brochure</title>
<link rel="stylesheet" href="https://fonts.googleapis.com/css2?family=Montserrat:wght@300;400;500;600;700&display=swap">
<style>
  :root {
    --rose: #b8797a;
    --rose-deep: #a86566;
    --rose-light: #e8c4c4;
    --rose-pale: #f4dedd;
    --band-top: #dcaeae;
    --band-bottom: #b57576;
    --ink: #2b2b2b;
    --text: #4a4a4a;
    --grey: #8e8e90;
    --grey-light: #c9c9cb;
    --paper: #ffffff;
    --stage: #e4e4e6;
    --leaf: #5e8f3a;
    --mint: #8fc4b3;
  }
  * { box-sizing: border-box; margin: 0; padding: 0; }
  html, body { width: 750px; height: 1200px; overflow: hidden; }
  body {
    background: var(--stage);
    font-family: 'Montserrat', sans-serif;
    color: var(--text);
    position: relative;
  }
  .spread {
    position: absolute;
    left: 15px;
    width: 720px;
    height: 540px;
    display: flex;
    box-shadow: 0 6px 20px rgba(0,0,0,.12);
  }
  .spread--outside { top: 40px; }
  .spread--inside { top: 620px; }
  .panel {
    position: relative;
    width: 240px;
    height: 540px;
    background: var(--paper);
    overflow: hidden;
  }
  .panel + .panel { border-left: 1px solid #eeeeee; }
  .band {
    position: absolute;
    left: 0; right: 0; bottom: 0;
    height: 120px;
    background: linear-gradient(180deg, var(--band-top), var(--band-bottom));
  }
  .brand-mark {
    font-family: 'Montserrat', sans-serif;
    font-weight: 400;
    color: var(--rose);
    letter-spacing: 2px;
    text-align: center;
    text-transform: uppercase;
    white-space: nowrap;
  }
  .product-name { text-align: center; font-weight: 300; line-height: 1; }
  .product-name .first { display: block; color: var(--rose); letter-spacing: 3px; }
  .product-name .second { display: block; color: var(--ink); letter-spacing: 6px; }
  .visual { position: absolute; }

  /* Outside: flap */
  .flap-kicker {
    position: absolute; top: 26px; left: 0; right: 0;
    text-align: center; color: var(--rose);
    font-size: 10px; line-height: 1.3; font-weight: 400;
  }
  .flap-headline {
    position: absolute; top: 56px; left: 0; right: 0;
    text-align: center; color: var(--ink);
    font-size: 18px; letter-spacing: 2px; font-weight: 400;
  }
  .flap .visual {
    top: 88px; left: 28px; width: 184px; height: 110px;
    background: radial-gradient(circle at 65% 35%, #e8f5f1 0 12%, transparent 30%),
                linear-gradient(135deg, #d7ece6, var(--mint) 55%, #5f9a88);
  }
  .flap .product-name { position: absolute; top: 214px; left: 0; right: 0; }
  .flap .product-name .first { font-size: 30px; }
  .flap .product-name .second { font-size: 22px; }
  .flap-tagline {
    position: absolute; top: 276px; left: 0; right: 0;
    text-align: center; font-size: 10px; color: var(--ink);
  }
  .distributor {
    position: absolute; top: 304px; left: 26px; width: 188px; height: 108px;
    background: var(--paper); border: 1px solid var(--rose-light);
    font-size: 10px; color: var(--ink); text-align: center; padding-top: 10px;
    z-index: 1;
  }

  /* Outside: back */
  .back .visual {
    top: 70px; left: 30px; width: 180px; height: 200px;
    background: radial-gradient(ellipse at 55% 45%, #f3dccd 0 35%, #f7ece6 55%, var(--paper) 75%);
  }
  .back .brand-mark { position: absolute; top: 296px; left: 0; right: 0; font-size: 11px; }
  .contact {
    position: absolute; left: 0; right: 0; bottom: 0; height: 120px;
    text-align: center; color: var(--ink); padding-top: 18px;
  }
  .contact-call { font-size: 11px; letter-spacing: 1px; }
  .contact-phone { font-size: 20px; font-weight: 400; letter-spacing: 1px; margin: 4px 0 6px; }
  .contact-web { font-size: 9px; }
  .contact-phone svg { width: 14px; height: 14px; vertical-align: -1px; margin-right: 4px; }

  /* Outside: cover */
  .cover .brand-mark { position: absolute; top: 44px; left: 0; right: 0; font-size: 13px; letter-spacing: 2px; }
  .cover .visual {
    top: 96px; left: 36px; width: 168px; height: 150px;
    background: radial-gradient(circle at 35% 75%, #f1f1f1 0 18%, transparent 30%),
                radial-gradient(circle at 70% 75%, #eeeeee 0 16%, transparent 28%),
                radial-gradient(ellipse at 50% 35%, #8ab86a 0 25%, #c8ddb8 50%, var(--paper) 72%);
  }
  .cover .product-name { position: absolute; top: 282px; left: 0; right: 0; }
  .cover .product-name .first { font-size: 34px; }
  .cover .product-name .second { font-size: 26px; }
  .cover-claim {
    position: absolute; left: 0; right: 0; bottom: 0; height: 120px;
    padding: 24px 14px 0; text-align: center;
    color: var(--ink); font-size: 14px; line-height: 1.35;
  }

  /* Inside: science panel */
  .science {
    background: linear-gradient(180deg, #d69d9e 0%, #e6bdbd 55%, var(--rose-pale) 100%);
    padding: 26px 20px 0;
    color: var(--paper);
  }
  .science-title { font-size: 13px; font-weight: 600; line-height: 1.3; letter-spacing: .5px; }
  .science-subtitle { font-size: 9.5px; font-weight: 700; color: var(--ink); margin-bottom: 12px; }
  .ingredient { margin-bottom: 22px; }
  .ingredient-name {
    display: inline-block; background: var(--rose-pale); color: var(--rose-deep);
    font-size: 10px; font-weight: 600; padding: 3px 12px 3px 8px; border-radius: 10px;
    margin-bottom: 7px;
  }
  .ingredient p { font-size: 8px; line-height: 1.45; color: var(--text); text-align: justify; }
  .science .brand-mark {
    position: absolute; bottom: 64px; left: 0; right: 0;
    font-size: 12px; color: #d4a5a5; letter-spacing: 2px;
  }

  /* Inside: benefits */
  .benefits .visual {
    top: 0; left: 0; width: 120px; height: 360px;
    background: linear-gradient(90deg, #e9d1c6, #f2e3db 60%, var(--paper));
  }
  .benefits-title {
    position: absolute; top: 210px; left: 108px;
    font-weight: 300; line-height: 1.05;
  }
  .benefits-title .lead { display: block; font-size: 14px; color: var(--ink); }
  .benefits-title .name { display: block; font-size: 22px; color: var(--rose); }
  .benefit-list {
    position: absolute; top: 318px; left: 30px; width: 180px; height: 200px;
    background: linear-gradient(180deg, #a9a9ab, var(--grey));
    border-radius: 12px; list-style: none; padding: 16px 12px;
  }
  .benefit-list li {
    font-size: 7.5px; font-weight: 600; color: var(--paper); text-transform: uppercase;
    line-height: 1.3; margin-bottom: 9px; padding-left: 10px; position: relative;
  }
  .benefit-list li::before {
    content: ""; position: absolute; left: 0; top: 3px; width: 4px; height: 4px;
    border-radius: 50%; background: var(--rose-light);
  }

  /* Inside: results */
  .results { padding: 26px 18px 0; }
  .chart-title { font-size: 8px; color: var(--ink); margin-bottom: 6px; }
  .chart { display: block; }
  .chart-caption {
    background: var(--rose); color: var(--paper); font-size: 5.5px;
    padding: 3px 5px; margin: 4px 0 12px;
  }
  .result-note { font-size: 8px; line-height: 1.45; color: var(--ink); }
  .results .visual {
    bottom: 0; right: 0; width: 110px; height: 76px;
    background: radial-gradient(circle at 40% 70%, #efefef 0 22%, transparent 34%),
                radial-gradient(circle at 75% 62%, #ececec 0 20%, transparent 32%),
                radial-gradient(ellipse at 85% 25%, #8ab86a 0 18%, #d4e4c6 40%, var(--paper) 70%);
  }
  .results .result-note--second {
    position: absolute; left: 18px; top: 398px; width: 204px;
    z-index: 1;
  }
</style>
</head>
<body>

<section class="spread spread--outside" aria-label="Brochure outside">
  <article class="panel flap">
    <p class="flap-kicker">One of the first Skin<br>&amp; Sun Protection</p>
    <h2 class="flap-headline">ALL IN ONE</h2>
    <div class="visual" role="img" aria-label="Translucent mint green supplement capsules"></div>
    <h1 class="product-name"><span class="first">VELVET</span><span class="second">DAWN</span></h1>
    <p class="flap-tagline">Nature's solution to skin whitening</p>
    <div class="distributor">Distributed by:</div>
    <div class="band"></div>
  </article>

  <article class="panel back">
    <div class="visual" role="img" aria-label="Portrait of a woman touching her glowing skin"></div>
    <p class="brand-mark">La douceur de Fenor</p>
    <div class="band"></div>
    <div class="contact">
      <p class="contact-call">CALL US TODAY</p>
      <p class="contact-phone"><svg viewBox="0 0 24 24" aria-hidden="true"><path fill="#2b2b2b" d="M6.6 10.8a15.1 15.1 0 0 0 6.6 6.6l2.2-2.2c.3-.3.7-.4 1-.2 1.1.4 2.3.6 3.6.6.6 0 1 .4 1 1V20c0 .6-.4 1-1 1A17 17 0 0 1 3 4c0-.6.4-1 1-1h3.5c.6 0 1 .4 1 1 0 1.3.2 2.5.6 3.600.1.3 0 .7-.2 1z"/></svg>555 014 2260</p>
      <p class="contact-web">www.fenorcare.com</p>
    </div>
  </article>

  <article class="panel cover">
    <p class="brand-mark">La douceur de Fenor</p>
    <div class="visual" role="img" aria-label="Fern leaf with two white tomatoes"></div>
    <h1 class="product-name"><span class="first">VELVET</span><span class="second">DAWN</span></h1>
    <div class="band"></div>
    <p class="cover-claim">Skin Whitening &amp;<br>Sun Protection all in one<br>Oral supplements</p>
  </article>
</section>

<section class="spread spread--inside" aria-label="Brochure inside">
  <article class="panel science">
    <h2 class="science-title">SKIN WHITENING &amp;<br>SUN PROTECTION:</h2>
    <p class="science-subtitle">THE SCIENTIFIC ANSWER</p>
    <div class="ingredient">
      <h3 class="ingredient-name">1) PhytoBloom</h3>
      <p>An award winning natural supplement using non-GMO tomato species rich in colourless carotenoids, phytoene and phytofluene. This patented combination provides superior whitening, UVA and UVB protection, anti-inflammatory and antioxidant properties.</p>
    </div>
    <div class="ingredient">
      <h3 class="ingredient-name">2) Polypodium leucotomos</h3>
      <p>Naturally extracted from a tropical natural fern found in the Americas, it has been used for centuries by the natives for its superior benefits. Now clinically proven to protect against UV radiation due to its antioxidant, anti-inflammatory and DNA repair abilities.</p>
    </div>
    <div class="ingredient">
      <h3 class="ingredient-name">3) L-Cysteine</h3>
      <p>A potent amino acid that has very high skin-whitening abilities. It prevents the production of pigment cells when the skin is exposed to UV rays and stimulates the production of Glutathione, another strong skin-whitening antioxidant.</p>
    </div>
    <p class="brand-mark">La douceur de Fenor</p>
  </article>

  <article class="panel benefits">
    <div class="visual" role="img" aria-label="Half portrait of a woman with smooth radiant skin"></div>
    <h2 class="benefits-title"><span class="lead">Benefits of</span><span class="name">VELVET<br>DAWN</span></h2>
    <ul class="benefit-list">
      <li>Skin whitening</li>
      <li>Collagen protection</li>
      <li>DNA repair</li>
      <li>Prevents against premature skin aging</li>
      <li>Enhanced antioxidant &amp; anti-inflammatory effects</li>
      <li>Natural UV protection</li>
    </ul>
  </article>

  <article class="panel results">
    <p class="chart-title">Average Clinical improvement of skin parameters</p>
    <svg class="chart" width="204" height="110" viewBox="0 0 204 110" aria-label="Bar chart of skin parameter improvement at day 42 and day 84">
      <g font-family="Montserrat, sans-serif" font-size="4" fill="#4a4a4a">
        <line x1="22" y1="4" x2="22" y2="90" stroke="#bbb" stroke-width=".5"/>
        <line x1="22" y1="90" x2="160" y2="90" stroke="#bbb" stroke-width=".5"/>
        <text x="19" y="91.5" text-anchor="end">0</text>
        <text x="19" y="74.3" text-anchor="end">20</text>
        <text x="19" y="57.1" text-anchor="end">40</text>
        <text x="19" y="39.9" text-anchor="end">60</text>
        <text x="19" y="22.7" text-anchor="end">80</text>
        <text x="19" y="5.5" text-anchor="end">100</text>
        <g fill="#b8797a">
          <rect x="28" y="42.7" width="7" height="47.3"/>
          <rect x="55" y="38.4" width="7" height="51.6"/>
          <rect x="82" y="42.7" width="7" height="47.3"/>
          <rect x="109" y="74.5" width="7" height="15.5"/>
          <rect x="136" y="70.2" width="7" height="19.8"/>
        </g>
        <g fill="#8e8e90">
          <rect x="37" y="31.5" width="7" height="58.5"/>
          <rect x="64" y="28.1" width="7" height="61.9"/>
          <rect x="91" y="21.2" width="7" height="68.8"/>
          <rect x="118" y="59.9" width="7" height="30.1"/>
          <rect x="145" y="44.4" width="7" height="45.6"/>
        </g>
        <text x="36" y="97" text-anchor="middle">Dryness</text>
        <text x="63" y="97" text-anchor="middle">Roughness</text>
        <text x="90" y="97" text-anchor="middle">Suppleness</text>
        <text x="117" y="97" text-anchor="middle">Complexion</text>
        <text x="144" y="97" text-anchor="middle">Texture</text>
        <rect x="166" y="36" width="30" height="22" fill="#fff" stroke="#ccc" stroke-width=".4"/>
        <rect x="169" y="40" width="4" height="4" fill="#b8797a"/>
        <text x="176" y="43.5">Day 42</text>
        <rect x="169" y="49" width="4" height="4" fill="#8e8e90"/>
        <text x="176" y="52.5">Day 84</text>
      </g>
    </svg>
    <p class="chart-caption">Figure 2: Graphic representation of the average changes in clinical scoring</p>
    <p class="result-note">Skin improvement results of a clinical study conducted by dermatologists measuring skin quality after 12 weeks use of colourless carotenoids (Journal of Skin Science 2015: 2(4) Page 178-182)</p>
    <svg class="chart" width="204" height="120" viewBox="0 0 204 120" style="margin-top:14px" aria-label="Bar chart showing a 42.1 percent reduction in melasma intensity">
      <g font-family="Montserrat, sans-serif" font-size="7" fill="#2b2b2b">
        <text x="120" y="14">-42.1%</text>
        <text x="120" y="30">p&lt;0.05</text>
        <line x1="40" y1="28" x2="40" y2="112" stroke="#2b2b2b" stroke-width=".8"/>
        <line x1="40" y1="112" x2="120" y2="112" stroke="#2b2b2b" stroke-width=".8"/>
        <text x="32" y="114" text-anchor="end">0</text>
        <text x="32" y="86" text-anchor="end">2</text>
        <text x="32" y="58" text-anchor="end">4</text>
        <text x="32" y="30" text-anchor="end">6</text>
        <rect x="54" y="30" width="26" height="82" fill="#b8797a"/>
        <rect x="80" y="56" width="26" height="56" fill="#8e8e90"/>
        <path d="M67 30 V22 H96 V44" fill="none" stroke="#2b2b2b" stroke-width="1"/>
        <path d="M92 40 L96 46 L100 40" fill="none" stroke="#2b2b2b" stroke-width="1"/>
      </g>
    </svg>
    <p class="result-note result-note--second">Reduction in intensity of melasma with usage of daily oral Polypodium Leucotomos for 12 weeks with sunscreen SPF 45 (Clinical Skin Reports 2012: 66(4) Page AB21).</p>
    <div class="visual" role="img" aria-label="Two white tomatoes with a fern leaf"></div>
  </article>
</section>

</body>
</html>
```